BrightForm /

We need a logo and letterhead for a startup Dental Laboratory in New Zealand. The business makes things like dentures, crowns, implants and night guards on prescription from dentists. The appliances are fabricated then shipped back to the dentist who recalls the patient and fits them. We are looking for a minimilist, very professional design. We don't want any play on words or mention of smiles or anything to do with apples. Would like the name to read
"BrightForm" and then a tag line " Precision Dental Laboratory"
Not that fussed on a logo other than maybe BF. The final design should communicate contemporary professionalism, innovation and an eye for detail.

```html
<!DOCTYPE html>
<html lang="en">
<head>
<meta charset="utf-8">
<title>BrightForm Letterhead</title>
<link href="https://fonts.googleapis.com/css2?family=Questrial&display=swap" rel="stylesheet">
<style>
  :root {
    --backdrop: #d3d3d5;
    --paper: #f5f5f5;
    --navy: #2f5677;
    --teal: #56a3bd;
    --ink: #3d3d3d;
    --ink-soft: #555;
    --rule: #bbbbbb;
    --signature-tone: #dde0ef;
  }
  * { margin: 0; padding: 0; box-sizing: border-box; }
  html, body { width: 1200px; height: 1152px; overflow: hidden; }
  body {
    background: var(--backdrop);
    font-family: "Questrial", "Century Gothic", sans-serif;
    color: var(--ink);
    position: relative;
  }
  .letterhead {
    position: absolute;
    left: 242px; top: 72px;
    width: 716px; height: 1008px;
    background: var(--paper);
    overflow: hidden;
  }
  .brand { position: absolute; left: 58px; top: 62px; }
  .brand-name {
    display: flex; align-items: center; gap: 7px;
    font-size: 31px; letter-spacing: 0.5px; line-height: 1;
    color: var(--navy);
  }
  .brand-mark { width: 12px; height: 12px; background: var(--teal); }
  .brand-tagline {
    margin-top: 6px; font-size: 10.5px; letter-spacing: 0.6px;
    color: var(--navy);
  }
  .contact { position: absolute; top: 66px; font-size: 10px; line-height: 12.8px; color: var(--ink-soft); font-style: normal; }
  .contact-address { left: 434px; }
  .contact-divider { position: absolute; left: 531px; top: 66px; width: 1px; height: 36px; background: var(--rule); }
  .contact-lines { left: 550px; }
  .contact-lines li { list-style: none; display: flex; align-items: center; gap: 6px; }
  .contact-lines svg { width: 10px; height: 10px; flex: none; }
  .date { position: absolute; left: 58px; top: 252px; font-size: 10.5px; }
  .recipient { position: absolute; left: 58px; top: 278px; font-size: 10.5px; line-height: 12.8px; font-style: normal; }
  .letter-body { position: absolute; left: 58px; top: 386px; width: 601px; font-size: 10.4px; line-height: 12.8px; }
  .salutation { font-weight: bold; margin-bottom: 13px; }
  .letter-body p.para { text-align: justify; margin-bottom: 12.8px; }
  .closing { position: absolute; left: 58px; top: 695px; font-size: 10.5px; line-height: 13px; }
  .closing strong { display: block; }
  .signature { position: absolute; left: 148px; top: 678px; width: 150px; height: 76px; background: var(--signature-tone); border-radius: 4px; }
  .footer-band { position: absolute; left: 0; bottom: 0; width: 716px; height: 22px; background: var(--navy); }
  .footer-line { position: absolute; left: 0; bottom: 26px; width: 716px; height: 3px; background: var(--teal); }
</style>
</head>
<body>
  <main class="letterhead">
    <header>
      <div class="brand">
        <div class="brand-name"><span>BrightForm</span><span class="brand-mark"></span></div>
        <div class="brand-tagline">Precision Dental Laboratory</div>
      </div>
      <address class="contact contact-address">
        18 Carlow Street<br>Level 2<br>Auckland 1010
      </address>
      <div class="contact-divider"></div>
      <ul class="contact contact-lines">
        <li>
          <svg viewBox="0 0 12 12"><rect width="12" height="12" rx="2" fill="#56a3bd"/><path d="M3.5 2.8c.4-.3.9-.2 1.1.2l.6 1.1c.2.3.1.7-.2.9l-.4.3c.4.9 1.1 1.6 2 2l.3-.4c.2-.3.6-.4.9-.2l1.1.6c.4.2.5.7.2 1.1l-.5.6c-2.9 0-5.6-2.7-5.6-5.6z" fill="#fff"/></svg>
          09.412.5530
        </li>
        <li>
          <svg viewBox="0 0 12 12"><rect width="12" height="12" rx="2" fill="#56a3bd"/><rect x="3.5" y="2.5" width="5" height="3" fill="#fff"/><rect x="2.5" y="5.5" width="7" height="3" fill="#fff"/><rect x="3.5" y="8" width="5" height="1.8" fill="#fff"/></svg>
          09.412.5531
        </li>
        <li>
          <svg viewBox="0 0 12 12"><rect width="12" height="12" rx="2" fill="#56a3bd"/><circle cx="6" cy="6" r="3.5" fill="none" stroke="#fff" stroke-width=".9"/><path d="M2.5 6h7M6 2.5c-1.6 2-1.6 5 0 7M6 2.5c1.6 2 1.6 5 0 7" fill="none" stroke="#fff" stroke-width=".7"/></svg>
          www.brightform.co.nz
        </li>
      </ul>
    </header>

    <div class="date">30.09.2016</div>
    <address class="recipient">Recipient's name<br>Lindenweg 7<br>20095 Hamburg<br>Germany</address>

    <section class="letter-body">
      <p class="salutation">Dear sir,</p>
      <p class="para">Communication is a very integral part of living creatures, animals and humans. Communication may be verbal or written. Written communication however is only applicable to human beings. Can you even imagine a world without communication? Verbal communication can be through telephones, webcams or in person. Written communication is through letters, emails and mobile phone messages.</p>
      <p class="para">In today's world of great inventions and technology, letters have somehow become redundant. It is the time for text messages or chats. But they still can communicate a lot more than all other modes of communication. Organizations and various government departments still bank on letters as a strong medium of communication. There is no comparison in costs of sending letters as compared to costs of mobile phone messages though – letters are far cheaper. Letters now commonly known as “hard copy documents” are considered more relevant and important than email copies of text messages as proof or evidence of some sort.</p>
      <p class="para">Letters speak volumes about a person or an organization that writes it. So one must take utmost care ensuring that the language used in any letter is appropriate for the occasion for which it is being written. Since a letter is also a written proof or document, if there are certain things that should not form a part of it, then that too should be carefully handled.</p>
      <p class="para">Writing a good letter is an art. But if for some reason someone is unable to write that perfect letter, these different types of letters provide a base for you to build on. Sample letters have been given for everyone to understand what all information needs to form a part of the letter type and then it can be customized.</p>
    </section>

    <div class="closing">Yours Sincerely,<strong>Elin Varrow</strong></div>
    <div class="signature" role="img" aria-label="Handwritten signature in blue ink"></div>

    <footer>
      <div class="footer-line"></div>
      <div class="footer-band"></div>
    </footer>
  </main>
</body>
</html>
```